Postcard flyers for text vouchers

Postcard flyer to drive people to text for local vouchers delivered straight to their mobile, alternatively they can check out the websites.
Double sided, full colour A6 size. 105mm x 148.5mm http://www.brindleprint.example/artwork-guide.html
Postcard will be available in high footfall areas must be eye catching and compelling, but keep message simple. Wording as attached, side one headline grabbing, side two in style of a tag cloud giving a flavour of vouchers/savings available in their local area.
Updates

Project Deadline Extended
Reason: Research has shown wider area for website required therefore by county [Hollowmere Vouchers] rather than smaller regions. Focus on entertainment and shopping for flyer.

Target Market(s)

Target 18-55 year olds
Core 25-45???
male and female

Requirements
Must have
• Stand out

```html
<!DOCTYPE html>
<html lang="en">
<head>
<meta charset="utf-8">
<title>How Much Can You Save? – Postcard Flyer</title>
<link rel="stylesheet" href="https://fonts.googleapis.com/css2?family=Arimo:wght@400;700&family=Alfa+Slab+One&family=Rye&family=Londrina+Outline:wght@900&display=swap">
<style>
  :root {
    --page: #ffffff;
    --card: #dcdfcc;
    --ink: #111111;
    --red: #d9252f;
    --white: #ffffff;
    --splat: #ffffff;
  }
  * { margin: 0; padding: 0; box-sizing: border-box; }
  html, body { width: 845px; height: 1200px; overflow: hidden; background: var(--page); }
  .sheet { position: relative; width: 845px; height: 1200px; font-family: "Arimo", Arial, sans-serif; color: var(--ink); }

  .side-label { position: absolute; left: 55px; font-weight: 700; font-size: 21px; }
  .side-label--front { top: 12px; }
  .side-label--back { top: 1164px; }

  .postcard { position: absolute; left: 55px; width: 748px; background: var(--card); border: 1.5px solid #222; overflow: hidden; }
  .postcard--front { top: 69px; height: 530px; }
  .postcard--back { top: 616px; height: 528px; }

  .chevrons { position: absolute; }
  .chevrons--front { left: 568px; top: 76px; width: 100px; height: 46px; }
  .chevrons--back { left: 10px; top: 110px; width: 74px; height: 38px; }

  .headline-how { position: absolute; left: 12px; top: 70px; font-family: "Alfa Slab One", serif; font-weight: 400; font-size: 158px; line-height: 1; letter-spacing: -3px; white-space: nowrap; }
  .headline-much { position: absolute; left: 406px; top: 222px; font-family: "Rye", serif; font-size: 28px; letter-spacing: 3px; white-space: nowrap; }
  .splat { position: absolute; left: 40px; top: 246px; width: 190px; height: 172px; }
  .saving-badge { position: absolute; left: 94px; top: 296px; font-weight: 700; font-size: 54px; color: var(--red); letter-spacing: -2px; white-space: nowrap; }
  .saving-badge small { font-size: 30px; }
  .headline-save { position: absolute; left: 246px; top: 258px; font-family: "Londrina Outline", sans-serif; font-weight: 900; font-size: 126px; line-height: 1; color: var(--red); letter-spacing: 18px; white-space: nowrap; }
  .headline-q { position: absolute; left: 588px; top: 248px; font-family: "Alfa Slab One", serif; font-weight: 400; font-size: 118px; line-height: 1; }

  .offer-cloud { position: absolute; left: 0; right: 0; top: 437px; text-align: center; font-size: 17.5px; line-height: 21.5px; white-space: nowrap; }
  .offer-cloud .sep { display: inline-block; width: 4px; height: 15px; background: var(--ink); margin: 0 8px; vertical-align: -2px; }

  .back-heading { position: absolute; left: 0; right: 0; top: 74px; text-align: center; font-family: "Rye", serif; font-weight: 400; font-size: 18px; letter-spacing: 0.5px; white-space: nowrap; }
  .back-heading .tag { display: inline-block; background: var(--red); color: var(--white); font-family: "Arimo", sans-serif; font-weight: 700; font-size: 24px; line-height: 31px; padding: 0 6px; margin: 0 6px; letter-spacing: 0; }
  .instruction { position: absolute; left: 106px; top: 127px; font-family: "Rye", serif; font-size: 16px; letter-spacing: 0.3px; white-space: nowrap; }
  .area-list { position: absolute; left: 0; right: 0; top: 166px; list-style: none; text-align: center; font-weight: 700; font-size: 19px; line-height: 32px; white-space: nowrap; }
  .area-list .key { color: var(--red); }
  .redeem { position: absolute; left: 0; right: 0; top: 275px; text-align: center; font-family: "Rye", serif; font-size: 16px; line-height: 19px; letter-spacing: 1px; white-space: nowrap; }
  .terms { position: absolute; left: 0; right: 0; top: 329px; text-align: center; font-family: "Rye", serif; font-size: 19.5px; line-height: 26px; letter-spacing: 1px; white-space: nowrap; }
  .websites { position: absolute; left: 0; right: 0; top: 418px; text-align: center; color: var(--red); font-weight: 700; font-size: 18px; line-height: 22px; white-space: nowrap; }
  .websites .divider { margin: 0 16px; }
</style>
</head>
<body>
<main class="sheet">
  <div class="side-label side-label--front">front</div>

  <section class="postcard postcard--front">
    <svg class="chevrons chevrons--front" viewBox="0 0 100 46" aria-hidden="true">
      <polyline points="4,4 44,23 4,42" fill="none" stroke="var(--red)" stroke-width="2"/>
      <polyline points="50,4 90,23 50,42" fill="none" stroke="var(--red)" stroke-width="2"/>
    </svg>

    <h1 class="headline-how">HOW</h1>
    <div class="headline-much">MUCH CAN YOU</div>

    <svg class="splat" viewBox="0 0 212 158" preserveAspectRatio="none" role="img" aria-label="White paint splat behind the saving figure">
      <path d="M40 70 C20 60 10 90 30 96 C10 110 30 140 60 124 C80 150 120 152 140 130 C170 146 200 120 186 96 C210 80 200 50 176 56 C180 24 150 10 130 30 C110 4 70 10 72 40 C50 30 30 44 40 70 Z" fill="var(--splat)"/>
    </svg>
    <div class="saving-badge">50<small>%</small></div>

    <div class="headline-save">SAVE</div>
    <div class="headline-q">?</div>

    <p class="offer-cloud">
      Eating out<span class="sep"></span>Entertainment<span class="sep"></span>building/plumbing/home services huge discounts<br>
      Free Entry for Events<span class="sep"></span>Theatre Deals<span class="sep"></span>Furniture vouchers<br>
      Fashion Deals<span class="sep"></span>FREE sessions solicitors/accountants<span class="sep"></span>Insurance offers
    </p>
  </section>

  <section class="postcard postcard--back">
    <h2 class="back-heading">YOUR LOCAL MONEY SAVING <span class="tag">Vouchers</span> ARE WAITING FOR YOU</h2>

    <svg class="chevrons chevrons--back" viewBox="0 0 74 38" aria-hidden="true">
      <polyline points="4,4 33,19 4,34" fill="none" stroke="var(--red)" stroke-width="2"/>
      <polyline points="39,4 68,19 39,34" fill="none" stroke="var(--red)" stroke-width="2"/>
    </svg>
    <p class="instruction">SIMPLY CHOOSE YOUR AREA AND TEXT AS FOLLOWS:</p>

    <ul class="area-list">
      <li>For savings in Malvern text voucher <span class="key">m</span> to 84321</li>
      <li>For savings in Worcester text voucher <span class="key">w</span> to 84321</li>
      <li>For savings in Hereford text voucher <span class="key">h</span> to 84321</li>
    </ul>

    <p class="redeem">TO REDEEM SIMPLY QUOTE THE VOUCHER<br>CODE OR PRINT OFF. EASY!</p>

    <p class="terms">STANDARD TEXT RATES APPLY. NO SPAM POLICY.<br>UNSUBSCIBE AT ANY TIME.<br>SEE YOUR VOUCHER WEBSITES FOR EVEN MORE SAVINGS</p>

    <p class="websites">
      www.malvernsavers.example<span class="divider">|</span>www.worcestersavers.example<br>
      www.herefordsavers.example
    </p>
  </section>

  <div class="side-label side-label--back">back</div>
</main>
</body>
</html>
```